Brightwell Dwellings

Design a stylish Business card- we would like a businness card design that suits plastic business cards. Our card needs to show that we are tech savy and technology based so the design is crucial.

Target Market(s)

22-40

Industry/Entity Type

Plastic

Requirements
Must have
• attached is our logo. also double sided card would be nice.
my details

Callum Fenwright
Director
0461927345
www.brightwelldwellings.com.au
17 Marlow Crest Avenue, West Perth

```html
<!DOCTYPE html>
<html lang="en">
<head>
<meta charset="utf-8">
<title>Brightwell Dwellings – Business Card</title>
<link href="https://fonts.googleapis.com/css2?family=Open+Sans:wght@400;600;700&display=swap" rel="stylesheet">
<style>
  :root {
    --page-bg: #e9e7e4;
    --card-bg: #262527;
    --card-glow: #353436;
    --text-light: #f2f2f2;
    --accent-blue: #1f7fc4;
    --band-dark: #06121c;
    --band-mid: #0f4f72;
    --band-light: #2ab4e6;
  }
  * { box-sizing: border-box; margin: 0; padding: 0; }
  html, body {
    width: 1200px;
    height: 900px;
    overflow: hidden;
    background: var(--page-bg);
    font-family: "Open Sans", Arial, sans-serif;
  }
  .card-set {
    position: absolute;
    top: 306px;
    left: 74px;
    display: flex;
    gap: 32px;
  }
  .card {
    position: relative;
    width: 506px;
    height: 288px;
    border-radius: 14px;
    background: var(--card-bg);
    overflow: hidden;
    box-shadow: 0 6px 18px rgba(0,0,0,0.25);
  }
  .card--back {
    background: radial-gradient(circle at 50% 45%, var(--card-glow) 0%, var(--card-bg) 55%);
  }
  .card__band {
    position: absolute;
    left: 0; right: 0; bottom: 0;
    height: 34px;
    background: linear-gradient(90deg, var(--band-dark) 0%, var(--band-mid) 35%, var(--band-light) 100%);
    display: flex;
    align-items: center;
    justify-content: center;
  }
  .card__band-url {
    color: var(--text-light);
    font-size: 11px;
    letter-spacing: 0.2px;
  }
  .contact {
    position: absolute;
    left: 26px;
    top: 110px;
    color: var(--text-light);
    font-size: 14px;
    line-height: 19px;
  }
  .contact__name {
    color: var(--accent-blue);
    font-weight: 700;
  }
  .contact__role { margin-bottom: 26px; }
  .brand {
    position: absolute;
    display: flex;
    align-items: center;
    gap: 10px;
    color: var(--text-light);
    font-weight: 700;
    font-size: 23px;
    letter-spacing: 0.5px;
    white-space: nowrap;
  }
  .brand__mark {
    width: 14px;
    height: 14px;
    border-radius: 50%;
    background: var(--band-light);
    flex: none;
  }
  .brand--front { right: 24px; top: 110px; }
  .brand--back { left: 50%; top: 50%; transform: translate(-50%, -70%); font-size: 27px; }
</style>
</head>
<body>
  <main class="card-set">
    <section class="card card--front" aria-label="Card front">
      <div class="brand brand--front"><span class="brand__mark"></span>Brightwell Dwellings</div>
      <div class="contact">
        <p class="contact__name">Callum Fenwright</p>
        <p class="contact__role">Director</p>
        <p>Phone : 0461927345</p>
        <p>www.brightwelldwellings.com.au</p>
        <p>17 Marlow Crest Avenue, West Perth</p>
      </div>
      <div class="card__band"></div>
    </section>

    <section class="card card--back" aria-label="Card back">
      <div class="brand brand--back"><span class="brand__mark"></span>Brightwell Dwellings</div>
      <div class="card__band"><span class="card__band-url">www.brightwelldwellings.com.au</span></div>
    </section>
  </main>
</body>
</html>
```